Pine Ridge Traders, LLC- Global Beverage Company with 100% Cold Chain Logistics

Hey All, My Name is Dale, I am a young business owner in a competitive export space, but my niche is that I am shipping all of my beer around the world, "100% Cold Chain". This model is more costly, but it protects the integrity of the beer itself and will give folks in foreign countries the best representation of what US Craft Beer has to offer.

I am not a branding guy and don't claim to be one, I am a salesperson first, and will be referring to all of you to create something great that will be memorable.

I am looking for a basic Business Card Design for my Craft Beer Export company. I sell US Craft Beer in several countries around the globe. Austrailia, China, Taiwan, Chile, France, New Zealand... to name a few.

I am looking for a sleek, modern, and fresh design. Quickly!

Thanks for your consideration!

Cheers,

Dale

Target Market(s)

International

Contact Information for Business Card

Dale Corwin
Founder- Roving Hops Guy
Dale@PineRidgeTraders.example
@RovingHopsGuy- Instagram only
www.Pineridgetraders.example
@PineRidgeTradersAU- Instagram Only

Font styles to use
Serif

Colors
0592cd
ffffff

Requirements
Must have
• Name-
• Title-
• Email-
• Social Media Handle-
• Company Website-
Nice to have
• Nice Logo/ Images on Card
Should not have
• Tacky Beer Images

```html
<!DOCTYPE html>
<html lang="en">
<head>
<meta charset="utf-8">
<title>Pine Ridge Traders – Business Card</title>
<link rel="stylesheet" href="https://fonts.googleapis.com/css2?family=Cinzel:wght@500&family=Open+Sans:wght@400;700&family=Arimo:wght@400&display=swap">
<style>
  :root {
    --brand-blue: #0592cd;
    --paper: #ffffff;
    --ink: #333333;
    --muted-gray: #6f7478;
    --bar-gray: #a7adb1;
    --map-dark: #6c7a8c;
    --map-light: #c9ced6;
    --backdrop: #e9ebee;
  }
  * { margin: 0; padding: 0; box-sizing: border-box; }
  html, body { width: 1200px; height: 900px; overflow: hidden; }
  body { background: var(--backdrop); position: relative; font-family: "Open Sans", sans-serif; }

  .card {
    position: absolute;
    background: var(--paper);
    box-shadow: 0 6px 18px rgba(0,0,0,0.12);
    overflow: hidden;
  }
  .card-front { left: 177px; top: 73px; width: 589px; height: 365px; }
  .card-back  { left: 388px; top: 505px; width: 567px; height: 352px; }

  /* Front: brand block */
  .brand { position: absolute; left: 300px; top: 40px; width: 258px; text-align: center; }
  .brand-mark { width: 40px; height: 40px; background: var(--brand-blue); margin: 0 auto 16px; }
  .brand-name {
    font-family: "Cinzel", serif; font-weight: 500; color: var(--brand-blue);
    font-size: 30px; line-height: 32px; letter-spacing: 0.5px;
  }
  .brand-tagline {
    margin-top: 8px; font-size: 13.5px; color: var(--muted-gray); letter-spacing: 1.6px;
  }
  .brand-claim {
    position: absolute; left: 300px; width: 258px; top: 225px; text-align: center;
    font-weight: 700; font-size: 14px; color: var(--ink); letter-spacing: 0.3px;
  }

  /* Front: person */
  .accent-bar { position: absolute; width: 22px; }
  .accent-name { left: 0; top: 228px; height: 42px; background: var(--brand-blue); }
  .accent-contact-left { left: 0; top: 297px; height: 37px; background: var(--bar-gray); }
  .accent-contact-right { right: 0; top: 298px; height: 36px; background: var(--bar-gray); }

  .person { position: absolute; left: 31px; top: 226px; }
  .person-name {
    font-family: "Cinzel", serif; font-weight: 500; color: var(--brand-blue);
    font-size: 23px; line-height: 26px; letter-spacing: 0.5px;
  }
  .person-title { font-size: 16.5px; color: var(--ink); margin-top: 2px; }

  .contact-list { position: absolute; left: 32px; top: 298px; list-style: none; }
  .contact-item { display: flex; align-items: center; gap: 6px; font-size: 14.5px; color: var(--ink); line-height: 19px; }
  .contact-item svg { width: 12px; height: 12px; flex: none; }

  .social-handle {
    position: absolute; right: 36px; top: 305px;
    display: flex; align-items: center; gap: 6px; font-size: 14.5px; color: var(--ink);
  }
  .social-dot { width: 20px; height: 20px; border-radius: 50%; background: var(--brand-blue); }

  /* Back */
  .map-area {
    position: absolute; left: 0; top: 0; width: 100%; height: 295px;
    background: radial-gradient(ellipse at 50% 45%, var(--map-dark) 0%, var(--map-light) 55%, var(--paper) 85%);
    opacity: 0.75;
  }
  .markets-band {
    position: absolute; left: 0; bottom: 0; width: 100%; height: 57px;
    background: var(--brand-blue); color: var(--paper);
    font-family: "Arimo", sans-serif; font-size: 19px;
    display: flex; align-items: center; justify-content: center;
  }
</style>
</head>
<body>

  <section class="card card-front" aria-label="Business card front">
    <div class="brand">
      <div class="brand-mark"></div>
      <div class="brand-name">PINE RIDGE<br>TRADERS</div>
      <div class="brand-tagline">GLOBAL BEVERAGE COMPANY</div>
    </div>
    <div class="brand-claim">100% COLD CHAIN LOGISTICS</div>

    <div class="accent-bar accent-name"></div>
    <div class="person">
      <div class="person-name">DALE CORWIN</div>
      <div class="person-title">Founder - Roving Hops Guy</div>
    </div>

    <div class="accent-bar accent-contact-left"></div>
    <ul class="contact-list">
      <li class="contact-item">
        <svg viewBox="0 0 12 12" aria-hidden="true"><rect x="0.5" y="2" width="11" height="8" fill="#0592cd"/><path d="M0.5 2 L6 6.5 L11.5 2" fill="none" stroke="#fff" stroke-width="1"/></svg>
        Dale@PineRidgeTraders.example
      </li>
      <li class="contact-item">
        <svg viewBox="0 0 12 12" aria-hidden="true"><circle cx="6" cy="6" r="5.5" fill="#0592cd"/><path d="M6 0.5 V11.5 M0.5 6 H11.5" stroke="#fff" stroke-width="0.9"/><ellipse cx="6" cy="6" rx="2.5" ry="5.5" fill="none" stroke="#fff" stroke-width="0.9"/></svg>
        www.Pineridgetraders.example
      </li>
    </ul>

    <div class="social-handle">@RovingHopsGuy <span class="social-dot"></span></div>
    <div class="accent-bar accent-contact-right"></div>
  </section>

  <section class="card card-back" aria-label="Business card back">
    <div class="map-area" role="img" aria-label="Dotted world map in grey tones"></div>
    <div class="markets-band">Austrailia | China | Taiwan | Chile | France | New Zealand</div>
  </section>

</body>
</html>
```